Plakat für Hersteller von Maultaschen und Knödeln
Zielgruppe
Mit meiner Manufaktur Rinnfalten & Co stelle ich Maultaschen und Knödel her. Produziert wird mit hochwertigen, möglichst regionalen Zutaten und mit dem Anspruch, traditionelle Klassiker in zeitgemäßer Qualität anzubieten.
Im Mittelpunkt stehen Frische, Transparenz und ehrliches Handwerk. Die Produkte werden mit Sorgfalt hergestellt und sind für den direkten Verkauf auf dem Brunnwaldener Wochenmarkt bestimmt. Rinnfalten & Co verbindet bodenständige Küche mit regionaler Identität – unkompliziert, authentisch und genussorientiert.
Zielgruppe rund um den Brunnwaldener Wochenmarkt:
- Marktbesucher mit Qualitätsbewusstsein, die gezielt regionale und handwerklich hergestellte Lebensmittel kaufen
- Berufstätige und Familien, die hochwertige, frisch produzierte Gerichte für zu Hause suchen
- Genussorientierte Kundinnen und Kunden, die traditionelle Küche schätzen
- Seniorinnen und Senioren, die klassische Hausmannskost bevorzugen
- Regionalverbundenen Verbraucherinnen und Verbrauchern, die lokale Anbieter unterstützen möchten
Der Brunnwaldener Wochenmarkt zieht ein vielfältiges Publikum an, das Wert auf persönliche Beratung, Frische und nachvollziehbare Herkunft legt. Rinnfalten positioniert sich hier als authentischer, spezialisierter Anbieter für handgemachte Teigklassiker mit klarem kulinarischem Profil.
Aufgabenstellung
Das Plakat soll in A5, A4, A3 und A2 nutzbar sein und der Text soll austauschbar sein.
Das Plakat soll gut zum Wochenmarkt passen und ehrliches, qualitativ hochwertiges Handwerk ausdrücken und vor allem Lust auf Maultaschen und Knödel machen. Es soll zu meinen Marktstand (Monza Rot) und dem Logo passen. Das Logo soll sehr präsent sein.

```html
<!DOCTYPE html>
<html lang="de">
<head>
<meta charset="utf-8">
<title>Rinnfalten &amp; Co – Traditionelle Klassiker</title>
<link href="https://fonts.googleapis.com/css2?family=Merriweather:wght@900&family=Montserrat:wght@500;800&display=swap" rel="stylesheet">
<style>
  :root {
    --monza: #a8191f;
    --monza-light: #c8202a;
    --monza-deep: #9c161c;
    --monza-soft: #b8232a;
    --leaf: #8cc63f;
    --leaf-bright: #c6e02c;
    --white: #ffffff;
    --ink: #111111;
    --plate: #f4f2ee;
  }
  html, body {
    margin: 0;
    padding: 0;
    width: 839px;
    height: 1200px;
    overflow: hidden;
    background: var(--monza);
  }
  .poster {
    position: relative;
    width: 839px;
    height: 1200px;
    overflow: hidden;
    background: radial-gradient(ellipse at 70% 55%, var(--monza-light) 0%, var(--monza) 55%, var(--monza-deep) 100%);
    font-family: "Merriweather", Georgia, serif;
  }
  .side-pattern {
    position: absolute;
    left: 0; top: 0;
    width: 70px; height: 575px;
    background: linear-gradient(90deg, var(--monza-soft) 0%, var(--monza-soft) 55%, rgba(184,35,42,0) 100%);
    -webkit-mask-image: linear-gradient(180deg, #000 0%, #000 80%, transparent 100%);
    mask-image: linear-gradient(180deg, #000 0%, #000 80%, transparent 100%);
  }
  .bottom-pattern {
    position: absolute;
    left: 0; bottom: 0;
    width: 839px; height: 330px;
    background: linear-gradient(180deg, rgba(230,60,70,0) 0%, rgba(230,60,70,0.35) 40%, rgba(235,70,80,0.45) 100%);
  }
  .brand {
    position: absolute;
    left: 0; top: 135px;
    width: 839px;
    display: flex;
    justify-content: center;
    align-items: center;
    gap: 18px;
  }
  .brand-dot {
    width: 62px; height: 62px;
    border-radius: 50%;
    background: var(--leaf);
  }
  .brand-name {
    font-family: "Montserrat", Arial, sans-serif;
    font-weight: 500;
    font-size: 50px;
    color: var(--white);
    letter-spacing: 0.5px;
  }
  .headline {
    position: absolute;
    left: 0; top: 262px;
    width: 870px;
    margin: 0;
    text-align: center;
    font-weight: 900;
    line-height: 1;
  }
  .headline-top {
    display: block;
    font-size: 82px;
    color: var(--white);
    letter-spacing: -1px;
    text-shadow: 2px 3px 4px rgba(0,0,0,0.35);
  }
  .headline-main {
    display: block;
    margin-top: 4px;
    font-size: 116px;
    letter-spacing: -1px;
    color: var(--leaf);
    background: linear-gradient(90deg, #7fbf36, var(--leaf-bright) 55%, #86c23a);
    -webkit-background-clip: text;
    background-clip: text;
    -webkit-text-fill-color: transparent;
    filter: drop-shadow(2px 3px 3px rgba(0,0,0,0.35));
  }
  .tagline {
    position: absolute;
    right: 56px; top: 480px;
    margin: 0;
    text-align: right;
    font-weight: 900;
    font-size: 42px;
    line-height: 62px;
    color: var(--white);
    text-shadow: 2px 3px 4px rgba(0,0,0,0.35);
  }
  .dish {
    position: absolute;
    border-radius: 50%;
    box-shadow: 0 8px 18px rgba(0,0,0,0.35);
  }
  .dish-roast {
    left: -2px; top: 491px;
    width: 452px; height: 452px;
    background: radial-gradient(circle at 55% 55%, #8a3f1e 0%, #a5542a 25%, #e0b44a 42%, #c9a173 55%, var(--plate) 68%);
  }
  .dish-pockets {
    left: 414px; top: 680px;
    width: 500px; height: 500px;
    background: radial-gradient(circle at 55% 52%, #e6dc9a 0%, #d6c575 22%, #c98a3e 40%, #d9a466 52%, var(--plate) 62%);
  }
  .quality-note {
    position: absolute;
    left: 78px; top: 924px;
    width: 336px; height: 248px;
    transform: rotate(-4deg);
    background: linear-gradient(135deg, var(--leaf-bright), #96c83a);
    box-shadow: 0 6px 14px rgba(0,0,0,0.3);
    display: flex;
    align-items: center;
    justify-content: center;
    text-align: center;
    font-family: "Montserrat", Arial, sans-serif;
    font-weight: 800;
    font-size: 31px;
    line-height: 36px;
    letter-spacing: -0.5px;
    color: var(--ink);
    text-transform: uppercase;
    margin: 0;
  }
</style>
</head>
<body>
<main class="poster">
  <div class="side-pattern" role="img" aria-label="Dekoratives Wellenlinienmuster am linken Rand"></div>
  <div class="bottom-pattern" role="img" aria-label="Dekoratives Wellenlinienmuster in Hellrot"></div>

  <div class="brand">
    <span class="brand-dot"></span>
    <span class="brand-name">Rinnfalten &amp; Co</span>
  </div>

  <h1 class="headline">
    <span class="headline-top">TRADITIONELLE</span>
    <span class="headline-main">KLASSIKER</span>
  </h1>

  <p class="tagline">In Zeitgemäßer<br>Qualität<br>Anzubieten</p>

  <div class="dish dish-roast" role="img" aria-label="Foto: Teller mit Schmorbraten, Soße, zwei Knödeln und Sauerkraut"></div>
  <div class="dish dish-pockets" role="img" aria-label="Foto: Teller mit Maultaschen in Brühe, Schnittlauch und Röstzwiebeln"></div>

  <p class="quality-note">Produziert<br>wird mit<br>hochwertigen,<br>regionalen<br>Zutaten</p>
</main>
</body>
</html>
```